Forensic investigators looking for updated powerpoint design

Louisiana company called Bayline Analytics has an important upcoming meeting and needs a redesigned slideshow template. They are an engineering firm providing evaluation, reporting, and expert witness testimony on a variety of topics to support the litigation and insurance industries. The meeting in question will be held at a conference catering to insurance underwriters.

Target Market(s)

Upcoming tradeshow presentation

Industry/Entity Type

Insurance; TIC (Testing, Inspection, Certification)

Font styles to use
Sans Serif

Colors
0054AA
0677BA
7BADD7
CADEEF
E8F1F8
FFC000
F8CF3A
FAE287
FDF2CF
FEFAEE

Requirements
Must have
• Updated background template with examples of different layouts (bullet list w/ graphic, bullet list without, quote, large central photo, etc.), implementing company logo
Nice to have
• Visual motif that carries through powerpoint designs
Should not have
• No hexagons (old motif of parent company that we're moving away from)

```html
<!DOCTYPE html>
<html lang="en">
<head>
<meta charset="utf-8">
<title>Bayline Analytics – Presentation Template</title>
<link rel="stylesheet" href="https://fonts.googleapis.com/css2?family=Rubik:wght@500;700;800&family=Roboto:ital,wght@0,400;0,500;0,700;1,400&display=swap">
<style>
:root{
  --stage:#a9a9a9;
  --blue:#1c3aa3;
  --blue-deep:#0f2486;
  --blue-mid:#2f55c9;
  --blue-light:#7badd7;
  --yellow:#f4c22b;
  --yellow-soft:#fae287;
  --ink:#1d1d1f;
  --grey:#555a63;
  --paper:#ffffff;
  --paper-tint:#f3f5f9;
}
*{box-sizing:border-box;margin:0;padding:0}
html,body{width:1020px;height:1200px;overflow:hidden}
body{background:var(--stage);font-family:"Roboto",sans-serif;color:var(--ink);position:relative}
.slide{position:absolute;width:420px;height:236px;overflow:hidden;background:var(--paper);box-shadow:0 3px 10px rgba(0,0,0,.25)}
.col-a{left:82px}.col-b{left:518px}
.row-1{top:105px}.row-2{top:356px}.row-3{top:607px}.row-4{top:858px}

/* header */
.slide-head{position:absolute;left:0;top:0;width:100%;height:32px;background:var(--blue);display:flex;align-items:center}
.slide-head::before{content:"";position:absolute;left:0;top:0;width:10px;height:100%;background:var(--yellow)}
.slide-title{font-family:"Rubik",sans-serif;font-weight:700;color:#fff;font-size:13px;letter-spacing:.3px;margin-left:22px}
.brand{display:flex;align-items:center;gap:4px;font-family:"Rubik",sans-serif;font-weight:700;color:#fff;white-space:nowrap}
.brand-mark{background:#fff;display:inline-block}
.slide-head .brand{position:absolute;right:22px;font-size:9px}
.slide-head .brand-mark{width:7px;height:7px}

/* footer */
.slide-foot{position:absolute;left:37px;right:0;bottom:0;height:14px;background:var(--blue);display:flex;align-items:center;gap:12px;padding-left:14px;font-size:4.2px;color:#fff}
.slide-foot::before{content:"";position:absolute;left:0;top:0;width:5px;height:100%;background:var(--yellow)}
.foot-item{display:flex;align-items:center;gap:3px}
.foot-item svg{width:5px;height:5px}
.page-no{position:absolute;right:16px;bottom:7px;width:12px;height:12px;background:var(--yellow);font-size:4.5px;font-weight:700;display:flex;align-items:center;justify-content:center;color:var(--ink)}

.art{position:absolute}
.gear-wash{position:absolute;background:radial-gradient(circle at 60% 55%,#c9ccd3 0%,#e6e8ec 45%,rgba(255,255,255,0) 75%)}

/* title slide */
.title-slide{background:linear-gradient(120deg,#1b2f9a 0%,#1636ad 50%,#0c1f7a 100%)}
.title-slide .art{inset:0;background:radial-gradient(ellipse at 75% 30%,rgba(70,110,230,.55),rgba(20,40,140,0) 60%)}
.title-slide .brand{position:absolute;left:0;right:0;top:56px;justify-content:center;font-size:21px;gap:7px}
.title-slide .brand-mark{width:14px;height:14px}
.cover-title{position:absolute;left:0;right:0;top:110px;text-align:center;font-family:"Rubik",sans-serif;font-weight:700;color:#fff;font-size:17.5px;line-height:23px;letter-spacing:.3px}
.cover-date{position:absolute;left:0;right:0;top:170px;text-align:center;color:var(--yellow);font-size:8.5px;font-weight:500}

/* quote slide */
.q-question{position:absolute;left:28px;top:51px;font-size:10px;font-weight:700}
.q-body{position:absolute;left:29px;top:76px;width:234px;font-size:8px;line-height:13.8px;text-align:justify;color:var(--ink)}
.q-source{position:absolute;left:29px;top:155px;width:234px;font-size:7px;line-height:12.6px;font-style:italic;color:var(--grey)}

/* outline */
.outline{position:absolute;left:20px;top:54px;list-style:none}
.outline li{display:flex;align-items:center;gap:10px;height:16.5px;font-size:8.5px}
.outline .num{width:11px;height:11px;border-radius:50%;background:var(--yellow);font-size:4.6px;font-weight:700;display:flex;align-items:center;justify-content:center}
.outline-art{left:262px;top:57px;width:142px;height:142px;border-radius:50%;background:radial-gradient(circle at 50% 45%,#6f9cf0 0%,#1f47c4 45%,#0b1f7e 100%);box-shadow:0 0 0 6px rgba(150,170,230,.18)}

/* bullets */
.bullets{position:absolute;left:29px;top:60px;width:184px;list-style:none}
.bullets li{position:relative;padding-left:10px;font-size:8px;line-height:13.8px;text-align:justify;margin-bottom:10px}
.bullets li::before{content:"";position:absolute;left:0;top:5px;width:4.5px;height:4.5px;border-radius:50%;background:var(--yellow)}
.photo-frame{position:absolute;border:2px solid #fff;border-radius:6px;box-shadow:0 2px 8px rgba(0,0,0,.25)}
.decay-photo{left:240px;top:60px;width:156px;height:130px;background:linear-gradient(180deg,#7d8a93 0%,#9b6a4e 30%,#b9825e 55%,#8c3b1e 100%)}

/* statistic */
.stat-text{position:absolute;left:29px;top:52px;width:370px;font-size:8.2px;line-height:13.8px}
.stat-photo{left:40px;top:93px;width:335px;height:112px;background:linear-gradient(180deg,#6b6f73 0%,#a99877 40%,#d3b07d 70%,#8a7a66 100%)}

/* graph */
.checks{position:absolute;left:14px;top:52px;width:200px;list-style:none}
.checks li{display:flex;gap:8px;margin-bottom:11px}
.tick{flex:none;width:20px;height:20px;border-radius:50%;background:var(--yellow);display:flex;align-items:center;justify-content:center}
.tick svg{width:9px;height:9px}
.checks p{font-size:8px;line-height:13.8px;text-align:justify}
.chart{position:absolute;left:244px;top:66px;width:162px;height:130px}

/* divider */
.divider{background:linear-gradient(135deg,#1c36a8,#172f99)}
.divider .art{inset:0;background:radial-gradient(circle at 40% 45%,rgba(90,120,220,.35),rgba(0,0,0,0) 55%)}
.divider .brand{position:absolute;left:0;right:0;top:90px;justify-content:center;font-size:16px;gap:6px}
.divider .brand-mark{width:11px;height:11px}
.divider-title{position:absolute;left:91px;top:126px;width:238px;height:29px;background:var(--yellow);display:flex;align-items:center;justify-content:center;font-family:"Rubik",sans-serif;font-weight:700;font-size:16.5px;color:var(--blue);letter-spacing:.3px}

/* closing */
.closing{background:linear-gradient(135deg,#1a37b0,#1630a0)}
.closing .brand{position:absolute;left:32px;top:46px;font-size:15px;gap:6px}
.closing .brand-mark{width:10px;height:10px}
.contacts{position:absolute;left:32px;top:84px;list-style:none;color:#fff;font-size:6px;line-height:10.4px}
.contacts li{display:flex;gap:7px;margin-bottom:8px}
.c-ico{flex:none;width:12px;height:12px;border-radius:50%;background:#fff;display:flex;align-items:center;justify-content:center}
.contacts li:nth-child(2) .c-ico{background:var(--yellow)}
.c-ico svg{width:6px;height:6px}
.thanks{position:absolute;left:0;top:184px;width:230px;height:38px;background:var(--yellow);font-family:"Rubik",sans-serif;font-weight:800;font-size:29px;color:var(--blue);display:flex;align-items:center;padding-left:15px;letter-spacing:.3px}
.closing-photo{left:205px;top:14px;width:203px;height:209px;border:2px solid var(--yellow);border-radius:10px;background:radial-gradient(circle at 50% 40%,#8ea6ff 0%,#4a5fe8 40%,#2530b5 100%)}
</style>
</head>
<body>

<!-- cover -->
<section class="slide title-slide col-a row-1">
  <div class="art" role="img" aria-label="Blue technology backdrop with a profile silhouette and circuit graphics"></div>
  <div class="brand"><span class="brand-mark"></span>Bayline Analytics</div>
  <h1 class="cover-title">ENGINEERING . INSPECTION<br>FAILURE ANALYSIS</h1>
  <p class="cover-date">FEBRUARY 10,2026</p>
</section>

<!-- quote -->
<section class="slide col-b row-1">
  <header class="slide-head"><h2 class="slide-title">WOOD DECAY (ROT)</h2><div class="brand"><span class="brand-mark"></span>Bayline Analytics</div></header>
  <div class="gear-wash" style="left:250px;top:34px;width:170px;height:190px" role="img" aria-label="Grey engineering gears illustration"></div>
  <p class="q-question">How long does it take for a piece of wood to decay?</p>
  <p class="q-body">"There is no way even to crudely estimate the rate of wood decay or its age. Wood decay is a complex biological phenomenon subject to many physical and environmental factors, such as moisture level, temperature, wood species, fungus species, geographic locality, and climate"</p>
  <p class="q-source">Marian T. Holloway, Biological Technician with the Coastal Timber Research Laboratory - Reference: Decay Keeps Working - All it takes is some wood and a little moisture - By Dale Fenwick, July 12, 1999.</p>
  <footer class="slide-foot">
    <span class="foot-item"><svg viewBox="0 0 10 10"><path d="M1 2l3-1 2 1 3-1v7l-3 1-2-1-3 1z" fill="var(--yellow)"/></svg>Bayline Analytics Main Office 418 Harborview Lane ,Kenner, LA 70065, Map</span>
    <span class="foot-item"><svg viewBox="0 0 10 10"><path d="M2 1l2 0 1 2-1 1a6 6 0 0 0 2 2l1-1 2 1v2c-4 0-7-3-7-7z" fill="var(--yellow)"/></svg>(504) 555-0142 Office</span>
    <span class="foot-item"><svg viewBox="0 0 10 10"><rect x="1" y="2" width="8" height="6" fill="var(--yellow)"/></svg>hello@baylineanalytics.com</span>
  </footer>
  <span class="page-no">05</span>
</section>

<!-- outline -->
<section class="slide col-a row-2">
  <header class="slide-head"><h2 class="slide-title">COURSE OUTLINE</h2><div class="brand"><span class="brand-mark"></span>Bayline Analytics</div></header>
  <ol class="outline">
    <li><span class="num">01</span>Purpose</li>
    <li><span class="num">02</span>Wood decay - "Biodeterioration"</li>
    <li><span class="num">03</span>How long does it take for a piece of wood to decay?</li>
    <li><span class="num">04</span>Mold, Decay and Fungus</li>
    <li><span class="num">05</span>Types of decay</li>
    <li><span class="num">06</span>Necessary Ingredients and Optimum Conditions</li>
    <li><span class="num">07</span>Sources of Moisture</li>
    <li><span class="num">08</span>Important Points</li>
    <li><span class="num">09</span>Results of Moisture Exposure Tests</li>
  </ol>
  <div class="art outline-art" role="img" aria-label="Circular blue image of a hand with a magnifier over a fingerprint"></div>
  <footer class="slide-foot">
    <span class="foot-item"><svg viewBox="0 0 10 10"><path d="M1 2l3-1 2 1 3-1v7l-3 1-2-1-3 1z" fill="var(--yellow)"/></svg>Bayline Analytics Main Office 418 Harborview Lane ,Kenner, LA 70065, Map</span>
    <span class="foot-item"><svg viewBox="0 0 10 10"><path d="M2 1l2 0 1 2-1 1a6 6 0 0 0 2 2l1-1 2 1v2c-4 0-7-3-7-7z" fill="var(--yellow)"/></svg>(504) 555-0142 Office</span>
    <span class="foot-item"><svg viewBox="0 0 10 10"><rect x="1" y="2" width="8" height="6" fill="var(--yellow)"/></svg>hello@baylineanalytics.com</span>
  </footer>
  <span class="page-no">02</span>
</section>

<!-- bullets with photo -->
<section class="slide col-b row-2">
  <header class="slide-head"><h2 class="slide-title">DECAY</h2><div class="brand"><span class="brand-mark"></span>Bayline Analytics</div></header>
  <div class="gear-wash" style="left:0;top:120px;width:110px;height:116px" role="img" aria-label="Grey gears decoration"></div>
  <div class="gear-wash" style="left:300px;top:70px;width:120px;height:166px" role="img" aria-label="Grey gears decoration"></div>
  <ul class="bullets">
    <li>Decay fungus may appear as fan-shaped patches, strands, or root-like structures that are usually white or brown in color.</li>
    <li>Sometimes fruiting bodies are produced that take the form of mushrooms, brackets, or crusts. The fungus, in the form of microscopic, threadlike strands called hyphae, permeates the wood and uses parts of it as food.</li>
  </ul>
  <div class="art photo-frame decay-photo" role="img" aria-label="Photo of rotting wood sill with white fungal growth beneath a window"></div>
  <footer class="slide-foot">
    <span class="foot-item"><svg viewBox="0 0 10 10"><path d="M1 2l3-1 2 1 3-1v7l-3 1-2-1-3 1z" fill="var(--yellow)"/></svg>Bayline Analytics Main Office 418 Harborview Lane ,Kenner, LA 70065, Map</span>
    <span class="foot-item"><svg viewBox="0 0 10 10"><path d="M2 1l2 0 1 2-1 1a6 6 0 0 0 2 2l1-1 2 1v2c-4 0-7-3-7-7z" fill="var(--yellow)"/></svg>(504) 555-0142 Office</span>
    <span class="foot-item"><svg viewBox="0 0 10 10"><rect x="1" y="2" width="8" height="6" fill="var(--yellow)"/></svg>hello@baylineanalytics.com</span>
  </footer>
  <span class="page-no">06</span>
</section>

<!-- statistic -->
<section class="slide col-a row-3">
  <header class="slide-head"><h2 class="slide-title">INTERESTING STATISTIC</h2><div class="brand"><span class="brand-mark"></span>Bayline Analytics</div></header>
  <p class="stat-text">Current estimates show that replacement materials, needed to repair damage caused by rot alone, account for nearly 10 percent of U.S. annual wood production.(Gulf State Forestry Extension)</p>
  <div class="art photo-frame stat-photo" role="img" aria-label="Photo of stacked lumber bundles in a warehouse"></div>
  <footer class="slide-foot">
    <span class="foot-item"><svg viewBox="0 0 10 10"><path d="M1 2l3-1 2 1 3-1v7l-3 1-2-1-3 1z" fill="var(--yellow)"/></svg>Bayline Analytics Main Office 418 Harborview Lane ,Kenner, LA 70065, Map</span>
    <span class="foot-item"><svg viewBox="0 0 10 10"><path d="M2 1l2 0 1 2-1 1a6 6 0 0 0 2 2l1-1 2 1v2c-4 0-7-3-7-7z" fill="var(--yellow)"/></svg>(504) 555-0142 Office</span>
    <span class="foot-item"><svg viewBox="0 0 10 10"><rect x="1" y="2" width="8" height="6" fill="var(--yellow)"/></svg>hello@baylineanalytics.com</span>
  </footer>
  <span class="page-no">03</span>
</section>

<!-- graph -->
<section class="slide col-b row-3">
  <header class="slide-head"><h2 class="slide-title">OUR GRAPH</h2><div class="brand"><span class="brand-mark"></span>Bayline Analytics</div></header>
  <div class="gear-wash" style="left:330px;top:80px;width:90px;height:156px" role="img" aria-label="Grey gears decoration"></div>
  <ul class="checks">
    <li><span class="tick"><svg viewBox="0 0 10 10"><path d="M2 5l2 2 4-4" stroke="var(--blue)" stroke-width="1.4" fill="none"/></svg></span><p>Sed ut perspiciatis unde omnis iste natus error sit voluptatem accusantium doloremque laudantium, totaaque ipsa quae ab illo</p></li>
    <li><span class="tick"><svg viewBox="0 0 10 10"><path d="M2 5l2 2 4-4" stroke="var(--blue)" stroke-width="1.4" fill="none"/></svg></span><p>Sed ut perspiciatis unde omnis iste natus error sit voluptatem accusantium doloremque laudantium, totaaque ipsa quae ab illo</p></li>
    <li><span class="tick"><svg viewBox="0 0 10 10"><path d="M2 5l2 2 4-4" stroke="var(--blue)" stroke-width="1.4" fill="none"/></svg></span><p>Sed ut perspiciatis unde omnis iste natus error sit voluptatem accusantium doloremque laudantium, totaaque ipsa quae ab illo</p></li>
  </ul>
  <svg class="chart" viewBox="0 0 162 130" font-family="Roboto, sans-serif" font-size="3.6" fill="#444">
    <g text-anchor="end">
      <text x="8" y="124">0</text><text x="8" y="112.2">1</text><text x="8" y="100.4">2</text><text x="8" y="88.6">3</text><text x="8" y="76.8">4</text><text x="8" y="65">5</text><text x="8" y="53.2">6</text><text x="8" y="41.4">7</text><text x="8" y="29.6">8</text><text x="8" y="17.8">9</text><text x="8" y="6">10</text>
    </g>
    <line x1="13" y1="3" x2="13" y2="123" stroke="#999" stroke-width=".4"/>
    <line x1="13" y1="123" x2="158" y2="123" stroke="#999" stroke-width=".4"/>
    <rect x="20" y="69.9" width="9" height="53.1" fill="var(--yellow)"/>
    <rect x="43" y="64" width="9" height="59" fill="var(--blue)"/>
    <rect x="66" y="39.2" width="9" height="83.8" fill="var(--yellow)"/>
    <rect x="89" y="64" width="9" height="59" fill="var(--blue)"/>
    <rect x="112" y="69.9" width="9" height="53.1" fill="var(--yellow)"/>
    <rect x="135" y="39.2" width="9" height="83.8" fill="var(--blue)"/>
    <g text-anchor="middle">
      <text x="24.5" y="67">4.5%</text><text x="47.5" y="61">5%</text><text x="70.5" y="36">7.1%</text><text x="93.5" y="61">5%</text><text x="116.5" y="67">4.5%</text><text x="139.5" y="36">7.1%</text>
      <text x="24.5" y="128.5">2000</text><text x="47.5" y="128.5">2005</text><text x="70.5" y="128.5">2010</text><text x="93.5" y="128.5">2015</text><text x="116.5" y="128.5">2020</text><text x="139.5" y="128.5">2024</text>
    </g>
  </svg>
  <footer class="slide-foot">
    <span class="foot-item"><svg viewBox="0 0 10 10"><path d="M1 2l3-1 2 1 3-1v7l-3 1-2-1-3 1z" fill="var(--yellow)"/></svg>Bayline Analytics Main Office 418 Harborview Lane ,Kenner, LA 70065, Map</span>
    <span class="foot-item"><svg viewBox="0 0 10 10"><path d="M2 1l2 0 1 2-1 1a6 6 0 0 0 2 2l1-1 2 1v2c-4 0-7-3-7-7z" fill="var(--yellow)"/></svg>(504) 555-0142 Office</span>
    <span class="foot-item"><svg viewBox="0 0 10 10"><rect x="1" y="2" width="8" height="6" fill="var(--yellow)"/></svg>hello@baylineanalytics.com</span>
  </footer>
  <span class="page-no">07</span>
</section>

<!-- section divider -->
<section class="slide divider col-a row-4">
  <div class="art" role="img" aria-label="Faint blue technical circles and network lines"></div>
  <div class="brand"><span class="brand-mark"></span>Bayline Analytics</div>
  <h2 class="divider-title">SECTION DIVIDER TITLE</h2>
</section>

<!-- closing -->
<section class="slide closing col-b row-4">
  <div class="brand"><span class="brand-mark"></span>Bayline Analytics</div>
  <ul class="contacts">
    <li><span class="c-ico"><svg viewBox="0 0 10 10"><path d="M1 2l3-1 2 1 3-1v7l-3 1-2-1-3 1z" fill="var(--blue)"/></svg></span><span>Bayline Analytics Main Office<br>418 Harborview Lane<br>Kenner, LA 70065</span></li>
    <li><span class="c-ico"><svg viewBox="0 0 10 10"><path d="M2 1l2 0 1 2-1 1a6 6 0 0 0 2 2l1-1 2 1v2c-4 0-7-3-7-7z" fill="var(--blue)"/></svg></span><span>(504) 555-0142 Office<br>(888) 555-0187 Toll Free</span></li>
    <li><span class="c-ico"><svg viewBox="0 0 10 10"><rect x="2" y="3" width="6" height="5" fill="var(--blue)"/><rect x="3" y="1" width="4" height="2" fill="var(--blue)"/></svg></span><span>(888) 555-0199 Fax</span></li>
  </ul>
  <div class="thanks">THANK YOU</div>
  <div class="art closing-photo" role="img" aria-label="Blue-toned image of hands typing on a laptop under a digital security interface"></div>
</section>

</body>
</html>
```